The layout of the quarterly calendar for the online store

I need to design a quarterly calendar for the online store of sanitary ware velanstok.ru.
The size of the top margin 335 mm * 210 mm bottom margin 335 mm * 65 mm
http://pikrafo.ru/qZT8LMe4kRRPRX
The main advantages of is a wide range of products (over 50,000 SKU), great price offers and competent advice.
When looking at the layout should have a full understanding of the company. The main sales of our online store carries b2c. But the calendar will be disseminated in wholesale trading organizations with the ability to attract additional customers in the form of installation companies and retail business.
The file with the signature style and font used in this attached.

Требуется разработать дизайн квартального календаря для интернет магазина инженерной сантехники velanstok.ru.
Размер верхнего поля 335 мм * 210 мм, нижнего поля 335 мм * 65 мм
Основными преимуществами является обширный ассортимент товаров (более 50000 SKU), отличные ценовые предложения и грамотные консультации.
При взгляде на макет должно возникнуть полное понимание, чем занимается компания. Основные продажи ИМ осуществляет b2c. Но календарь планируется распространить в торгующих оптовых организациях, с возможностью привлечения доп клиентов в виде монтажных организаций и мелко-розничного бизнеса.
Файл с фирменным стилем и шрифтами, использующимися в нем прилагаю.

Target Market(s)

The majority of customers - retail customers. Male 25 to 40 years.
Основная масса клиентов ИМ - розница. Мужчина от 25 до 40 лет.

Industry/Entity Type

Store

Font styles to use
Other font styles liked:
• pf_din_display

Colors
f37122
0792cd
ec1f27

Requirements
Must have
• Understanding of belonging to the plumbing engineering (heating, water)
• Понимание принадлежности к инженерной сантехнике (отопление, водоснабжение)
Nice to have
• sample equipment from our website
• Возможно образцы оборудования
Should not have
• People and animals
• Животные и люди

```html
<!DOCTYPE html>
<html lang="en">
<head>
<meta charset="utf-8">
<title>Velanstok — Quarterly Calendar 2018</title>
<link href="https://fonts.googleapis.com/css2?family=Barlow:ital,wght@0,300;0,400;0,500;0,600;0,700;1,300;1,600;1,700&display=swap" rel="stylesheet">
<style>
:root{
  --orange:#f37122;
  --blue:#0792cd;
  --red:#ec1f27;
  --ink:#3a3a3a;
  --muted:#7a7a7a;
  --panel:#f2f2f2;
  --shade:#e6e6e6;
  --black:#111;
  --white:#fff;
}
*{margin:0;padding:0;box-sizing:border-box}
html,body{width:1200px;height:2250px;overflow:hidden;background:var(--white)}
body{font-family:"Barlow",Arial,sans-serif;color:var(--ink)}
.canvas{position:relative;width:1200px;height:2250px;overflow:hidden}
.sheet{position:absolute;left:210px;top:57px;width:783px;height:2118px;background:var(--panel)}

/* header */
.hero{position:absolute;left:210px;top:57px;width:783px;height:491px;overflow:hidden}
.hero-photo{position:absolute}
.hero-photo.floor{left:0;top:0;width:390px;height:240px;background:linear-gradient(135deg,#f4f4f4,#e7dcd2)}
.hero-photo.tools{left:393px;top:0;width:390px;height:240px;background:linear-gradient(160deg,#f3f5f7,#3a3a3a 35%,#1b1b1b)}
.hero-photo.pumps{left:0;top:243px;width:390px;height:248px;background:linear-gradient(135deg,#d8effa,#6cc4ec 60%,#4c6f8d)}
.hero-photo.radiators{left:393px;top:243px;width:390px;height:248px;background:linear-gradient(200deg,#bfe6f8,#4fb9e8 55%,#e8eef2)}
.hero-tag{position:absolute;background:rgba(255,255,255,.9);color:var(--red);font-size:24px;font-weight:400;padding:2px 8px;line-height:1.2}
.badge{position:absolute;left:243px;top:102px;width:296px;height:296px;border-radius:50%;background:var(--white);border:4px solid var(--red);text-align:center}
.badge-year{margin-top:48px;font-size:108px;font-weight:700;color:var(--blue);letter-spacing:2px;line-height:1}
.badge-brand{margin-top:18px;font-size:34px;font-weight:500;color:var(--ink);display:flex;align-items:center;justify-content:center;gap:10px}
.badge-brand .dot{width:26px;height:26px;border-radius:50%;background:var(--orange)}
.hanger{position:absolute;left:570px;top:27px;width:60px;height:60px;border-radius:50%;background:var(--black)}

/* month blocks */
.strip{position:absolute;left:210px;width:783px;height:42px;display:flex;align-items:center;gap:19px;padding-left:12px}
.strip i{display:block;width:21px;height:21px;background:var(--black)}
.strip.orange{background:var(--orange)}
.strip.blue{background:var(--blue)}
.rule{position:absolute;left:210px;width:783px;height:20px;background:var(--orange)}
.month-title{position:absolute;left:210px;height:56px;width:335px;display:flex;align-items:center;padding-left:16px;color:var(--white);font-size:46px;font-weight:700;font-style:italic;clip-path:polygon(0 0,100% 0,92% 100%,0 100%)}
.month-title.orange{background:var(--orange)}
.month-title.blue{background:var(--blue)}
.month-year{position:absolute;right:220px;font-size:62px;font-weight:300;font-style:italic;color:var(--red);line-height:1}
.sat-shade{position:absolute;left:867px;width:108px;background:var(--shade)}
.weekdays,.days{position:absolute;left:217px;width:756px;display:grid;grid-template-columns:repeat(7,108px);text-align:center}
.weekdays{font-size:34px;font-weight:300;color:var(--muted);border-bottom:1.5px solid #9a9a9a;padding-bottom:2px}
.weekdays .we{color:var(--orange)}
.days{grid-auto-rows:52px;font-size:36px;font-weight:600;line-height:52px}
.days .we{color:var(--orange)}

/* footer */
.footer-brand{position:absolute;left:245px;top:2060px;display:flex;align-items:center;gap:14px;font-size:46px;font-weight:500;color:#555}
.footer-brand .dot{width:44px;height:44px;border-radius:50%;background:var(--orange)}
.footer-divider{position:absolute;left:545px;top:2043px;width:2px;height:100px;background:#333}
.contacts{position:absolute;left:560px;top:2040px;color:var(--ink)}
.contact-phone{display:flex;align-items:center;gap:6px;font-size:33px;font-weight:400}
.contact-address{display:flex;gap:8px;font-size:18px;line-height:1.25;margin-top:8px}
.contact-links{display:flex;gap:34px;font-size:19px;margin-top:8px}
.contact-links span{display:flex;align-items:center;gap:6px}
svg.icon{flex:none}
</style>
</head>
<body>
<div class="canvas">
  <div class="sheet"></div>

  <header class="hero">
    <div class="hero-photo floor" role="img" aria-label="Rolled underfloor heating mat with orange grid"></div>
    <div class="hero-photo tools" role="img" aria-label="Open case of pipe mounting tools"></div>
    <div class="hero-photo pumps" role="img" aria-label="Centrifugal water pump on blue hexagon background"></div>
    <div class="hero-photo radiators" role="img" aria-label="Sectional heating radiator on blue background"></div>
    <svg style="position:absolute;left:389px;top:0" width="4" height="491"><rect width="4" height="491" fill="#fff"/></svg>
    <svg style="position:absolute;left:0;top:238px" width="783" height="6"><rect width="783" height="6" fill="#fff"/></svg>
    <span class="hero-tag" style="left:15px;top:203px">Warm floor</span>
    <span class="hero-tag" style="left:590px;top:200px">Mounting Tools</span>
    <span class="hero-tag" style="left:20px;top:430px">Pumps</span>
    <span class="hero-tag" style="left:643px;top:430px">Radiators</span>
    <div class="badge">
      <div class="badge-year">2018</div>
      <div class="badge-brand"><span class="dot"></span>Velanstok</div>
    </div>
  </header>
  <div class="hanger"></div>

  <!-- December 2017 -->
  <div class="strip orange" style="top:550px"><i></i><i></i><i></i><i></i><i></i><i></i><i></i><i></i><i></i><i></i><i></i><i></i><i></i><i></i><i></i><i></i><i></i><i></i><i></i></div>
  <div class="sat-shade" style="top:652px;height:365px"></div>
  <div class="month-title orange" style="top:596px">December</div>
  <div class="month-year" style="top:596px">2017</div>
  <div class="weekdays" style="top:662px"><span class="we">Sun</span><span>Mon</span><span>Tue</span><span>Wed</span><span>Thu</span><span>Fri</span><span class="we">Sat</span></div>
  <div class="days" style="top:710px">
    <span></span><span></span><span></span><span></span><span></span><span>1</span><span class="we">2</span>
    <span class="we">3</span><span>4</span><span>5</span><span>6</span><span>7</span><span>8</span><span class="we">9</span>
    <span class="we">10</span><span>11</span><span>12</span><span>13</span><span>14</span><span>15</span><span class="we">16</span>
    <span class="we">17</span><span>18</span><span>19</span><span>20</span><span>21</span><span>22</span><span class="we">23</span>
    <span class="we">24</span><span>25</span><span>26</span><span>27</span><span>28</span><span>29</span><span class="we">30</span>
    <span class="we">31</span>
  </div>
  <div class="rule" style="top:1017px"></div>

  <!-- January 2018 -->
  <div class="strip blue" style="top:1045px"><i></i><i></i><i></i><i></i><i></i><i></i><i></i><i></i><i></i><i></i><i></i><i></i><i></i><i></i><i></i><i></i><i></i><i></i><i></i></div>
  <div class="sat-shade" style="top:1148px;height:359px"></div>
  <div class="month-title blue" style="top:1092px">January</div>
  <div class="month-year" style="top:1090px">2018</div>
  <div class="weekdays" style="top:1152px"><span class="we">Sun</span><span>Mon</span><span>Tue</span><span>Wed</span><span>Thu</span><span>Fri</span><span class="we">Sat</span></div>
  <div class="days" style="top:1195px">
    <span></span><span>1</span><span>2</span><span>3</span><span>4</span><span>5</span><span class="we">6</span>
    <span class="we">7</span><span>8</span><span>9</span><span>10</span><span>11</span><span>12</span><span class="we">13</span>
    <span class="we">14</span><span>15</span><span>16</span><span>17</span><span>18</span><span>19</span><span class="we">20</span>
    <span class="we">21</span><span>22</span><span>23</span><span>24</span><span>25</span><span>26</span><span class="we">27</span>
    <span class="we">28</span><span>29</span><span>30</span><span>31</span>
  </div>
  <div class="rule" style="top:1507px"></div>

  <!-- February 2018 -->
  <div class="strip blue" style="top:1533px"><i></i><i></i><i></i><i></i><i></i><i></i><i></i><i></i><i></i><i></i><i></i><i></i><i></i><i></i><i></i><i></i><i></i><i></i><i></i></div>
  <div class="sat-shade" style="top:1635px;height:365px"></div>
  <div class="month-title blue" style="top:1580px">February</div>
  <div class="month-year" style="top:1580px">2018</div>
  <div class="weekdays" style="top:1643px"><span class="we">Sun</span><span>Mon</span><span>Tue</span><span>Wed</span><span>Thu</span><span>Fri</span><span class="we">Sat</span></div>
  <div class="days" style="top:1686px">
    <span></span><span></span><span></span><span></span><span>1</span><span>2</span><span class="we">3</span>
    <span class="we">4</span><span>5</span><span>6</span><span>7</span><span>8</span><span>9</span><span class="we">10</span>
    <span class="we">11</span><span>12</span><span>13</span><span>14</span><span>15</span><span>16</span><span class="we">17</span>
    <span class="we">18</span><span>19</span><span>20</span><span>21</span><span>22</span><span>23</span><span class="we">24</span>
    <span class="we">25</span><span>26</span><span>27</span><span>28</span>
  </div>
  <div class="rule" style="top:2000px"></div>

  <!-- footer -->
  <footer>
    <div class="footer-brand"><span class="dot"></span>Velanstok</div>
    <div class="footer-divider"></div>
    <div class="contacts">
      <div class="contact-phone">
        <svg class="icon" width="26" height="26" viewBox="0 0 24 24"><path fill="#f37122" d="M6.6 10.8a15.1 15.1 0 0 0 6.6 6.6l2.2-2.2c.3-.3.7-.4 1-.2 1.1.4 2.3.6 3.6.6.6 0 1 .4 1 1V20c0 .6-.4 1-1 1A17 17 0 0 1 3 4c0-.6.4-1 1-1h3.5c.6 0 1 .4 1 1 0 1.3.2 2.5.6 3.6.1.3 0 .7-.2 1z"/></svg>
        +7 495 210-47-36
      </div>
      <div class="contact-address">
        <svg class="icon" width="16" height="20" viewBox="0 0 16 20"><path fill="#f37122" d="M8 0a7 7 0 0 0-7 7c0 5 7 13 7 13s7-8 7-13a7 7 0 0 0-7-7zm0 9.5A2.5 2.5 0 1 1 8 4.5a2.5 2.5 0 0 1 0 5z"/></svg>
        <span>Moscow, st. Lesnaya, 12, 3, office 214,<br>(Business center "Severny")</span>
      </div>
      <div class="contact-links">
        <span><svg class="icon" width="20" height="14" viewBox="0 0 20 14"><rect width="20" height="14" rx="1" fill="#f37122"/><path d="M1 1l9 7 9-7" stroke="#fff" stroke-width="1.5" fill="none"/></svg>info@velanstok.ru</span>
        <span><svg class="icon" width="18" height="18" viewBox="0 0 18 18"><circle cx="9" cy="9" r="8" fill="#f37122"/><path d="M1 9h16M9 1c3 3 3 13 0 16M9 1c-3 3-3 13 0 16" stroke="#fff" stroke-width="1.2" fill="none"/></svg>www.velanstok.ru</span>
      </div>
    </div>
  </footer>
</div>
</body>
</html>
```